Pelloway Dental Care needs a functioning website with Wordpress

Our dental office needs a fully coded and functioning simple (3 page) website with Wordpress for us to be able to modify the content and add pages/tabs and be able to upload to Hostivo Linux hosting with cPanels for publication. The page should be professional, warm, inviting and easy to use and follow and content should be optimized for Zentrix search engine visibility. Please see the current temporary site for details of the office including contact info and mission: www.pellowaydentalcare.ca also see the attached files for logo and office photos.

Target Market(s)

Families

Industry/Entity Type

Dental Clinic

Coding

Coded - Design and coding required

Number of Pages Required

3 page

Font styles to use
Sans Serif

Requirements
Must have
• Wordpress coding, contact info, mission, photos, keywords and content for Zentrix search engine optimization, my logo, empty common tabs for us to be able to add content later such as services, hours, about us, etc.

```html
<!DOCTYPE html>
<html lang="en">
<head>
<meta charset="utf-8">
<title>Pelloway Dental Care</title>
<link href="https://fonts.googleapis.com/css2?family=Cinzel:wght@400;700&family=Lato:wght@400;700&family=Roboto+Condensed:wght@400;700&family=Kalam:wght@700&display=swap" rel="stylesheet">
<style>
:root{
  --green:#7dc12b;
  --green-dark:#5f9c18;
  --ink:#2b2b2b;
  --grey-text:#8a8a8a;
  --mid-grey:#777;
  --panel:#f1f1f1;
  --footer:#6b6b6b;
  --white:#fff;
}
*{margin:0;padding:0;box-sizing:border-box}
html,body{width:890px;height:1200px;overflow:hidden;background:var(--white)}
body{position:relative;font-family:"Lato",sans-serif;color:var(--ink)}
.abs{position:absolute}

/* header */
.site-header{top:0;left:0;width:890px;height:68px;background:var(--white)}
.brand{left:102px;top:16px;display:flex;align-items:center;gap:8px}
.brand-dot{width:26px;height:26px;border-radius:50%;background:var(--green)}
.brand-name{font-family:"Lato",sans-serif;font-weight:700;font-size:20px;color:var(--green)}
.call{right:99px;top:9px;display:flex;align-items:center;gap:6px;font-size:10px;color:var(--mid-grey)}
.call strong{font-size:15px;color:var(--green);font-weight:700}
.main-nav{right:99px;top:43px;display:flex;font-family:"Cinzel",serif;font-size:12px;letter-spacing:.5px}
.main-nav a{color:var(--mid-grey);text-decoration:none;padding:0 13px;border-left:1px solid #ddd}
.main-nav a:first-child{border:0}
.main-nav a:last-child{padding-right:0}
.main-nav a.active{color:var(--green)}

/* hero */
.hero{top:68px;left:0;width:890px;height:366px;
  background:linear-gradient(100deg,#8a9a6a 0%,#b7c29a 35%,#d9c7a8 55%,#e8d6a4 75%,#dfe2cf 100%)}
.hero-title{left:100px;top:120px;font-family:"Kalam",cursive;font-weight:700;font-size:25px;line-height:40px;color:var(--white)}
.btn-appt{left:100px;top:282px;height:36px;display:flex;align-items:center}
.btn-appt .icon{width:36px;height:36px;border-radius:50%;background:#2f2f2f;border:2px solid var(--white);display:flex;align-items:center;justify-content:center;z-index:1}
.btn-appt .label{margin-left:-6px;height:30px;padding:0 14px 0 18px;background:var(--green);border:1px solid #d6efb5;border-radius:0 4px 4px 0;font-family:"Roboto Condensed",sans-serif;font-weight:700;font-size:16px;line-height:28px;color:var(--white)}
.arrow{top:245px;width:14px;height:28px}

/* feature band */
.features{top:390px;left:0;width:890px;height:197px;background:var(--panel)}
.feature{top:448px;width:200px;text-align:center}
.feature .ring{margin:0 auto;width:84px;height:84px;border-radius:50%;background:var(--green);border:5px solid var(--white);box-shadow:0 0 0 4px var(--green),0 6px 4px rgba(0,0,0,.15);display:flex;align-items:center;justify-content:center}
.feature h3{margin-top:18px;font-family:"Roboto Condensed",sans-serif;font-size:15px;font-weight:400;color:var(--ink)}

/* about */
.section-title{left:0;width:890px;text-align:center;font-family:"Roboto Condensed",sans-serif;font-size:19px;color:var(--mid-grey)}
.section-title .name{font-family:"Cinzel",serif;color:var(--green);font-size:23px;margin:0 6px}
.rule{left:120px;width:652px;border-top:1px dashed #ccc}
.rule-mark{width:10px;height:10px;border-radius:50%;border:1px solid #999;background:var(--white)}
.portrait{left:107px;top:676px;width:111px;height:128px;background:linear-gradient(90deg,#5a1f1a,#8a5a48 60%,#6e7f8e);border:2px solid var(--white);box-shadow:0 0 2px rgba(0,0,0,.3)}
.bio{left:233px;top:680px;width:555px;font-size:9.5px;line-height:15px;color:var(--grey-text)}
.bio h4{font-size:11px;color:var(--ink);margin-bottom:1px}
.bio h4 span{color:var(--green);font-weight:400}
.bio p{margin-bottom:8px}
.btn-dark{display:inline-block;margin-top:3px;padding:2px 7px;background:#222;border-radius:2px;color:var(--white);font-weight:700;font-size:9.5px}

/* services */
.services{top:828px;left:0;width:890px;height:170px;background:repeating-linear-gradient(45deg,#efefef 0 2px,#e9e9e9 2px 4px)}
.sunburst{left:80px;top:830px;width:200px;height:160px;background:radial-gradient(circle at 60px 90px,#ffffff 0,#d9d9d9 70%,rgba(233,233,233,0) 100%)}
.services-title{left:274px;top:840px;font-family:"Lato",sans-serif;font-size:21px;color:var(--mid-grey)}
.services-title .name{font-family:"Cinzel",serif;color:var(--green);font-size:23px}
.svc-col{top:894px;list-style:none;font-size:11.5px;color:var(--ink)}
.svc-col li{height:25px;display:flex;align-items:center;gap:7px}
.tick{width:10px;height:10px;border-radius:50%;background:var(--green);display:flex;align-items:center;justify-content:center}

/* footer */
.footer{top:990px;left:0;width:890px;height:178px;background:var(--footer)}
.btn-green{left:527px;top:986px;width:131px;height:23px;background:var(--green);border:1px solid #d6efb5;border-radius:3px;color:var(--white);font-family:"Roboto Condensed",sans-serif;font-weight:700;font-size:12px;line-height:21px;text-align:center}
.foot-h{font-family:"Cinzel",serif;font-size:14px;color:var(--white);letter-spacing:.5px;padding-bottom:6px;border-bottom:1px solid #888}
.quick{left:99px;top:1020px;width:92px}
.quick ul{list-style:none;font-size:9.5px;color:var(--white)}
.quick li{height:24.5px;line-height:24px;border-bottom:1px solid #888;padding-left:10px;position:relative}
.quick li::before{content:"";position:absolute;left:1px;top:9px;border-left:4px solid var(--white);border-top:3px solid transparent;border-bottom:3px solid transparent}
.quick li:last-child{border:0}
.contact{left:230px;top:1020px;width:313px}
.contact .rows{width:180px;font-size:9.5px;color:var(--white);line-height:14px}
.contact .row{display:flex;gap:10px;padding:6px 0;border-bottom:1px solid #888}
.contact .row:last-child{border:0}
.contact .row.phone{font-weight:700;font-size:11px}
.map{left:420px;top:1054px;width:132px;height:83px;background:linear-gradient(135deg,#e4e2dc,#efece6 60%,#cfd9e6);border:2px solid var(--white)}
.hours{left:605px;top:1040px;width:178px}
.hours .list{margin-top:8px;font-size:10px;color:var(--white);line-height:16.5px}
.bottom-bar{top:1168px;left:0;width:890px;height:32px;background:var(--green);color:var(--white);font-size:9.5px}
.copy{left:99px;top:10px}
.follow{right:99px;top:7px;display:flex;align-items:center;gap:7px;font-weight:700}
.follow i{width:17px;height:17px;border-radius:3px;background:rgba(255,255,255,.35);display:block}
</style>
</head>
<body>

<header class="site-header abs">
  <div class="brand abs"><span class="brand-dot"></span><span class="brand-name">Pelloway Dental Care</span></div>
  <div class="call abs">
    <svg width="18" height="18" viewBox="0 0 18 18"><circle cx="9" cy="9" r="8" fill="none" stroke="#999"/><path d="M6 5c-1 1 0 4 2 6s5 3 6 2l-2-2-1 1c-1 0-3-2-3-3l1-1z" fill="#999"/></svg>
    Call Us Today <strong>905-555-0148</strong>
  </div>
  <nav class="main-nav abs">
    <a class="active" href="#">Home</a><a href="#">About Us</a><a href="#">Services</a><a href="#">Contact Us</a>
  </nav>
</header>

<section class="hero abs" role="img" aria-label="Photo of a smiling young couple outdoors among green trees"></section>
<svg class="arrow abs" style="left:54px" viewBox="0 0 14 28"><path d="M13 1L1 14l12 13" fill="none" stroke="#fff" stroke-width="1.5"/></svg>
<svg class="arrow abs" style="right:54px" viewBox="0 0 14 28"><path d="M1 1l12 13L1 27" fill="none" stroke="#fff" stroke-width="1.5"/></svg>
<div class="hero-title abs">Beautiful Smile for successful life<br>Your Smile is our Priority</div>
<div class="btn-appt abs">
  <span class="icon"><svg width="18" height="18" viewBox="0 0 18 18"><rect x="1" y="3" width="13" height="12" fill="none" stroke="#fff" stroke-width="1.4"/><path d="M1 6h13M4 1v3M11 1v3" stroke="#fff" stroke-width="1.4"/><circle cx="13" cy="13" r="4" fill="#2f2f2f" stroke="#fff" stroke-width="1.2"/><path d="M13 11v2h2" stroke="#fff" fill="none"/></svg></span>
  <span class="label">Make An Appointment</span>
</div>

<div class="features abs"></div>
<svg class="abs" style="left:0;top:380px" width="890" height="60" viewBox="0 0 890 60">
  <path d="M0 14 C200 2 420 50 620 52 C740 53 820 24 890 20 L890 60 L0 60Z" fill="#f1f1f1"/>
  <path d="M0 14 C200 2 420 50 620 52 C740 53 820 24 890 20" fill="none" stroke="#7dc12b" stroke-width="5"/>
</svg>

<div class="feature abs" style="left:102px">
  <div class="ring"><svg width="36" height="40" viewBox="0 0 36 40"><path d="M4 8c3-7 10-6 14-3 4-3 11-4 14 3 2 6-1 11-2 16-1 6-2 14-6 14-3 0-3-9-6-9s-3 9-6 9c-4 0-5-8-6-14C5 19 2 14 4 8z" fill="#fff"/></svg></div>
  <h3>Cosmetic Dentistry</h3>
</div>
<div class="feature abs" style="left:345px">
  <div class="ring"><svg width="46" height="26" viewBox="0 0 46 26"><path d="M2 4c14 4 28 4 42 0-3 14-12 20-21 20S5 18 2 4z" fill="#fff"/><path d="M8 8h30M23 7v9M16 7v8M30 7v8" stroke="#7dc12b" stroke-width="1.5"/></svg></div>
  <h3>Teeth Whitening</h3>
</div>
<div class="feature abs" style="left:595px">
  <div class="ring"><svg width="24" height="40" viewBox="0 0 24 40"><path d="M2 4c3-4 7-3 10-1 3-2 7-3 10 1 1 5-1 9-2 11H4C3 13 1 9 2 4z" fill="#fff"/><path d="M7 18h10l-2 18h-6z" fill="#fff"/><path d="M7 22h10M7 26h10M8 30h8" stroke="#7dc12b" stroke-width="1.5"/></svg></div>
  <h3>Snore Reduction Appliances</h3>
</div>

<h2 class="section-title abs" style="top:610px">ABOUT<span class="name">PELLOWAY</span>DENTAL CARE</h2>
<div class="rule abs" style="top:650px"></div>
<div class="rule-mark abs" style="left:440px;top:645px"></div>
<div class="portrait abs" role="img" aria-label="Portrait photo of the dentist"></div>
<div class="bio abs">
  <h4><span>Daniel R. Ashcombe, DDS</span> (Specialized In Dentist)</h4>
  <p>Lorem ipsum dolor sit amet, consectetur adipiscing elit. Fusce dignissim libero in pretium rutrum. Nunc ut quam elementum, bibend quam vel, tristique dui. Maecenas semper nunc et fringilla ullamcorper.</p>
  <p>Fusce non aliquam augue. Phasellus mattis ultrices libero, sed ullamcorper ante laoreet ut. Nullam sodales lorem in pretium molestie. Fusce dolor turpis, dignissim nec tempus ut, lacinia id lacus.</p>
  <span class="btn-dark">Read More</span>
</div>

<section class="services abs"></section>
<div class="sunburst abs" role="img" aria-label="Soft grey light-burst decoration"></div>
<h2 class="services-title abs"><span class="name">PELLOWAY</span> DENTAL CARE Services We Offer</h2>
<div class="rule abs" style="left:274px;width:430px;top:880px"></div>
<div class="rule-mark abs" style="left:476px;top:875px"></div>
<ul class="svc-col abs" style="left:282px">
  <li><span class="tick"><svg width="6" height="6" viewBox="0 0 6 6"><path d="M1 3l1.5 1.5L5 1.5" stroke="#fff" fill="none"/></svg></span>Examinations &amp; Cleaning</li>
  <li><span class="tick"><svg width="6" height="6" viewBox="0 0 6 6"><path d="M1 3l1.5 1.5L5 1.5" stroke="#fff" fill="none"/></svg></span>Children´s Dentistry</li>
  <li><span class="tick"><svg width="6" height="6" viewBox="0 0 6 6"><path d="M1 3l1.5 1.5L5 1.5" stroke="#fff" fill="none"/></svg></span>Dentures And Partials</li>
</ul>
<ul class="svc-col abs" style="left:444px">
  <li><span class="tick"><svg width="6" height="6" viewBox="0 0 6 6"><path d="M1 3l1.5 1.5L5 1.5" stroke="#fff" fill="none"/></svg></span>Tooth Whitening &amp; Reshaping</li>
  <li><span class="tick"><svg width="6" height="6" viewBox="0 0 6 6"><path d="M1 3l1.5 1.5L5 1.5" stroke="#fff" fill="none"/></svg></span>Tooth Colored Fillings</li>
  <li><span class="tick"><svg width="6" height="6" viewBox="0 0 6 6"><path d="M1 3l1.5 1.5L5 1.5" stroke="#fff" fill="none"/></svg></span>Snore Reduction Appliances</li>
</ul>
<ul class="svc-col abs" style="left:627px">
  <li><span class="tick"><svg width="6" height="6" viewBox="0 0 6 6"><path d="M1 3l1.5 1.5L5 1.5" stroke="#fff" fill="none"/></svg></span>Bite And TMJ Appliances</li>
  <li><span class="tick"><svg width="6" height="6" viewBox="0 0 6 6"><path d="M1 3l1.5 1.5L5 1.5" stroke="#fff" fill="none"/></svg></span>Dental Implant Restorations</li>
  <li><span class="tick"><svg width="6" height="6" viewBox="0 0 6 6"><path d="M1 3l1.5 1.5L5 1.5" stroke="#fff" fill="none"/></svg></span>Root Canal Therapy</li>
</ul>

<footer class="footer abs"></footer>
<svg class="abs" style="left:0;top:970px" width="890" height="60" viewBox="0 0 890 60">
  <path d="M0 0 H890 V26 C800 26 700 50 560 56 C380 60 200 14 0 8Z" fill="#ececec"/>
  <path d="M0 8 C200 14 380 60 560 56 C700 50 800 26 890 26" fill="none" stroke="#7dc12b" stroke-width="4"/>
</svg>
<div class="btn-green abs">Make An Appointment</div>

<div class="quick abs">
  <h5 class="foot-h">QUICK LINKS</h5>
  <ul><li>Home</li><li>About Us</li><li>Services</li><li>Contact Us</li></ul>
</div>
<div class="contact abs">
  <h5 class="foot-h">CONTACT DETAILS</h5>
  <div class="rows">
    <div class="row"><svg width="10" height="13" viewBox="0 0 10 13"><path d="M5 0a5 5 0 00-5 5c0 4 5 8 5 8s5-4 5-8a5 5 0 00-5-5z" fill="#fff"/><circle cx="5" cy="5" r="2" fill="#6b6b6b"/></svg><span>12-40 Linden Grove Road,<br>Pelloway, ON L6C 2R4</span></div>
    <div class="row phone"><svg width="10" height="13" viewBox="0 0 10 13"><rect x="1.5" y="0.5" width="7" height="12" rx="1" fill="none" stroke="#fff"/><circle cx="5" cy="10.5" r=".8" fill="#fff"/></svg><span>905-555-0148</span></div>
    <div class="row"><svg width="11" height="13" viewBox="0 0 11 13"><rect x=".5" y="3" width="10" height="7" fill="#fff"/><path d="M.5 3l5 4 5-4" stroke="#6b6b6b" fill="none"/></svg><span>reception@pellowaydentalcare.ca</span></div>
  </div>
</div>
<div class="map abs" role="img" aria-label="Street map showing the clinic location"></div>
<div class="hours abs">
  <h5 class="foot-h">HOURS OF OPERATION</h5>
  <div class="list">Monday to Friday :&nbsp; 9:00 am to 6:00 pm<br>Saturday :&nbsp; 12:00 pm to 6:00 pm<br>Sunday :&nbsp; Closed</div>
</div>

<div class="bottom-bar abs">
  <span class="copy abs">© 2016 PELLOWAY Dental Care.&nbsp; All rights reserved.</span>
  <span class="follow abs">Follow Us: <i></i><i></i><i></i><i></i></span>
</div>

</body>
</html>
```